Etiketten für Wein
Zielgruppe
Weinkellerei aus Baden (Deutschland) mit Fokus im Lebensmittelhandel in Deutschland
Zielgruppe: Discount-Kunden, Männlich/Weiblich, Alter: 25-60 Jahre, wird für unter € 4,-/Fl. verkauft.
Aufgabenstellung
Wir suchen ein Frontetikett für einen Riesling aus Rheinhessen. Das Etikett sollte zeitlos, schlicht, modern anmutend sein. Hochwertiges Etikettenpapier (zweiteilig).
Weinbeschreibung:
Aussehen: helles gelb,
Geruch: Frische Frucht, heimische und exotische Früchte,
Geschmack: Feines Spiel von Frucht und animierender Säure
Anforderungen Etikett:
Maße: Höhe max. 120mm/Breite max. 80mm (darf auch kleiner oder quadratisch sein)
SK Etikett, Naturstruktur bis 90g (m²) (gerne zweiteilig)
Eine figürliche Etikettenkontur ist möglich, es wird aber am rechten Etikettenrand eine gerade Spendekante benötigt um das Etikett maschinell verarbeiten zu können.
Als Flasche wird eine 0,75 L Schlegelflasche (Farbe: feuille morte) eingesetzt.
Verschluss: Longcap
Mögliche Veredelungen: Quelllack, Prägungen, Heissfolie, Glanzlack
Pflichtangaben:
- Rheinhessen
- Auerbacher Lindenhang Riesling Qualitätswein trocken (Rebsorte 'Riesling' gerne prominent darstellen)
- Jahrgang 2023
SK Etikett, Naturstruktur bis 90g (m²) (gerne zweiteilig - einteilig aber auch möglich)

```html
<!DOCTYPE html>
<html lang="de">
<head>
<meta charset="utf-8">
<title>Auerbacher Lindenhang Riesling – Etiketten</title>
<link rel="stylesheet" href="https://fonts.googleapis.com/css2?family=Open+Sans:wght@400&family=PT+Serif:wght@400&display=swap">
<style>
  :root {
    --page: #ffffff;
    --ink: #3a3a3a;
    --gold: #c9a96a;
    --gold-deep: #a5844a;
    --grey-dark: #737373;
    --grey-light: #dedede;
    --white-a: #fbfbfb;
    --white-b: #e4e5e5;
  }
  * { box-sizing: border-box; margin: 0; padding: 0; }
  html, body { width: 1200px; height: 1200px; overflow: hidden; background: var(--page); }
  .sheet {
    position: relative; width: 1200px; height: 1200px;
    display: flex; justify-content: space-around; align-items: flex-start;
    padding: 70px 60px 0;
  }
  .variant { position: relative; width: 360px; height: 1080px; }
  .variant--silver { --bg: linear-gradient(90deg, var(--grey-dark), var(--grey-light)); --riesling: var(--gold); }
  .variant--white { --bg: linear-gradient(90deg, var(--white-a), var(--white-b)); --riesling: var(--ink); }

  .capsule {
    position: absolute; left: 110px; top: 0; width: 120px; height: 340px;
    background: var(--bg); box-shadow: 0 0 0 1px rgba(0,0,0,.06);
  }
  .capsule__text {
    position: absolute; right: 14px; bottom: 18px;
    writing-mode: vertical-rl; transform: rotate(180deg);
    font: 400 12px/1 "Open Sans", sans-serif; letter-spacing: .06em; color: var(--ink);
  }
  .disc {
    position: absolute; left: 258px; top: 140px; width: 100px; height: 100px; border-radius: 50%;
    background: var(--bg); box-shadow: 0 0 0 1px rgba(0,0,0,.08);
    display: flex; align-items: center; justify-content: center;
  }
  .disc__motif, .label__motif {
    border-radius: 50%;
    background: radial-gradient(circle, var(--gold-deep) 0%, var(--gold) 35%, rgba(201,169,106,.35) 65%, rgba(201,169,106,0) 72%);
  }
  .disc__motif { width: 56px; height: 56px; }

  .label {
    position: absolute; left: 0; top: 420px; width: 360px; height: 540px;
    background: var(--bg); box-shadow: 0 0 0 1px rgba(0,0,0,.06);
    display: flex; flex-direction: column; align-items: center; text-align: center;
    color: var(--ink);
  }
  .label__motif { width: 200px; height: 250px; margin-top: 26px; border-radius: 50% 50% 46% 46%; }
  .label__site { margin-top: 40px; font: 400 16px/1 "Open Sans", sans-serif; letter-spacing: .09em; }
  .label__variety { margin-top: 20px; font: 400 17px/1 "Open Sans", sans-serif; letter-spacing: .1em; color: var(--riesling); }
  .label__facts { margin-top: 20px; font: 400 10.5px/1.7 "PT Serif", serif; text-transform: uppercase; }
  .label__vintage { margin-top: 12px; font: 400 11px/1 "PT Serif", serif; }
  .label__mark { margin-top: auto; margin-bottom: 0; width: 26px; height: 24px; background: linear-gradient(135deg, var(--gold), var(--gold-deep)); }
</style>
</head>
<body>
<main class="sheet">

  <section class="variant variant--silver">
    <div class="capsule"><span class="capsule__text">AUERBACHER LINDENHANG</span></div>
    <div class="disc"><div class="disc__motif" role="img" aria-label="Goldene Spirale als Kopfmotiv"></div></div>
    <article class="label">
      <div class="label__motif" role="img" aria-label="Goldenes Spiralmotiv in Heißfolie"></div>
      <p class="label__site">AUERBACHER LINDENHANG</p>
      <p class="label__variety">RIESLING</p>
      <p class="label__facts">Rheinhessen<br>Qualitätswein<br>Trocken</p>
      <p class="label__vintage">2023</p>
      <span class="label__mark"></span>
    </article>
  </section>

  <section class="variant variant--white">
    <div class="capsule"><span class="capsule__text">AUERBACHER LINDENHANG</span></div>
    <div class="disc"><div class="disc__motif" role="img" aria-label="Goldene Spirale als Kopfmotiv"></div></div>
    <article class="label">
      <div class="label__motif" role="img" aria-label="Goldenes Spiralmotiv in Heißfolie"></div>
      <p class="label__site">AUERBACHER LINDENHANG</p>
      <p class="label__variety">RIESLING</p>
      <p class="label__facts">Qualitätswein<br>Rheinhessen<br>Trocken</p>
      <p class="label__vintage">2023</p>
      <span class="label__mark"></span>
    </article>
  </section>

</main>
</body>
</html>
```